I own a company on Maui, called Coral Haven and we are hosting our first LGBT Golf Tournament on Tuesday, June 9, 2015, titled The Rainbow Open 2015 and need a poster design enticing and inviting golf players to participate by playing in our 1st LGBT Golf Tournament, etc.
Updates

Aloha~ Since this poster is for a LGBT Golf Tournament, I will provide more detailed information as we go along. For example, times, dates, prizes, charity organization, etc. You may review both www.coralhaventours.example, the Host of the tournament and www.therainbowopen.example. the actual site for the tournament. If you have any questions, please contact me. Mahalo!

Industry/Entity Type

It Company

```html
<!DOCTYPE html>
<html lang="en">
<head>
<meta charset="utf-8">
<title>The Rainbow Open 2015 – Palm Cove Golf Course</title>
<link rel="stylesheet" href="https://fonts.googleapis.com/css2?family=Titan+One&family=Raleway:wght@300;400&display=swap">
<style>
  :root {
    --bg: #353535;
    --bg-flower: #424242;
    --bg-flower-deep: #3c3c3c;
    --ink: #f4f4f4;
    --ink-soft: #e4e4e4;
    --rule: #9a9a9a;
    --tee-light: #ededed;
    --tee-mid: #d2d2d2;
    --tee-shade: #a9a9a9;
  }
  * { box-sizing: border-box; margin: 0; padding: 0; }
  html, body {
    width: 927px;
    height: 1200px;
    overflow: hidden;
    background: var(--bg);
  }
  .poster {
    position: relative;
    width: 927px;
    height: 1200px;
    background: var(--bg);
    color: var(--ink);
    font-family: "Raleway", "Century Gothic", sans-serif;
    font-weight: 300;
    overflow: hidden;
  }
  .flower-pattern {
    position: absolute;
    left: 30px;
    top: 210px;
    width: 867px;
    height: 700px;
    border-radius: 120px;
    background:
      radial-gradient(ellipse 30% 40% at 20% 35%, var(--bg-flower) 0%, transparent 100%),
      radial-gradient(ellipse 30% 40% at 80% 35%, var(--bg-flower) 0%, transparent 100%),
      radial-gradient(ellipse 45% 35% at 50% 78%, var(--bg-flower-deep) 0%, transparent 100%);
  }
  .headline-arcs {
    position: absolute;
    left: 0;
    top: 0;
    width: 927px;
    height: 760px;
  }
  .event-title {
    font-family: "Titan One", "Arial Black", sans-serif;
    font-size: 74px;
    fill: var(--ink);
    letter-spacing: 2px;
  }
  .venue-name {
    font-family: "Titan One", "Arial Black", sans-serif;
    font-size: 47px;
    fill: var(--ink);
    letter-spacing: 1px;
  }
  .crossed-tees {
    position: absolute;
    left: 224px;
    top: 238px;
    width: 478px;
    height: 360px;
    border-radius: 60px;
    background:
      linear-gradient(135deg, var(--tee-light) 0%, var(--tee-mid) 50%, var(--tee-shade) 100%);
    opacity: 0.22;
  }
  .details {
    position: absolute;
    left: 0;
    top: 808px;
    width: 927px;
    list-style: none;
  }
  .detail-row {
    display: flex;
    align-items: center;
    padding: 0 27px;
    gap: 24px;
    height: 50px;
    font-size: 29px;
    letter-spacing: 0.5px;
  }
  .detail-row + .detail-row { margin-top: 33px; }
  .detail-row::before,
  .detail-row::after {
    content: "";
    flex: 1;
    height: 1px;
    background: var(--rule);
  }
  .detail-row--small { font-size: 21px; }
  .detail-row__text { white-space: nowrap; color: var(--ink-soft); }
  .more-info {
    position: absolute;
    left: 0;
    top: 1152px;
    width: 927px;
    text-align: center;
    font-size: 18px;
    color: var(--ink-soft);
    letter-spacing: 0.3px;
  }
  .more-info__url { font-size: 16px; font-weight: 400; }
</style>
</head>
<body>
  <main class="poster">
    <div class="flower-pattern" role="img" aria-label="Faint hibiscus flower pattern across the background"></div>

    <div class="crossed-tees" role="img" aria-label="Illustration of two crossed golf tees holding golf balls marked with small rainbow flags"></div>

    <svg class="headline-arcs" viewBox="0 0 927 760" aria-labelledby="event-title">
      <defs>
        <path id="title-arc" d="M 60 205 Q 463 95 866 205"/>
        <path id="venue-arc" d="M 110 640 Q 463 700 816 640"/>
      </defs>
      <text class="event-title" id="event-title" text-anchor="middle">
        <textPath href="#title-arc" startOffset="50%">THE RAINBOW OPEN</textPath>
      </text>
      <text class="venue-name" text-anchor="middle">
        <textPath href="#venue-arc" startOffset="50%">PALM COVE GOLF COURSE</textPath>
      </text>
    </svg>

    <ul class="details">
      <li class="detail-row"><span class="detail-row__text">TUESDAY, JUNE 9th, 2015</span></li>
      <li class="detail-row"><span class="detail-row__text">hosted by CORAL HAVEN</span></li>
      <li class="detail-row"><span class="detail-row__text">contests and prizes; grand prize: TRIP TO IRELAND</span></li>
      <li class="detail-row detail-row--small"><span class="detail-row__text">a portion of proceeds donated to THE HARBOR LIGHT PROJECT</span></li>
    </ul>

    <p class="more-info">for more information, please visit <span class="more-info__url">www.therainbowopen.example</span> or <span class="more-info__url">www.coralhaventours.example</span></p>
  </main>
</body>
</html>
```